Brightmoor Partners Branding Revamp

We are a consulting company, looking for a way to display and promote our brand. We have 2 sides to the business- Brightmoor (financial) and Partners (cyber security). The financial side products relate to business necessities: card processing, website design/hosting/maintenance, VoIP phone systems. The cyber security side promotes a bundled package of 4 solutions: network vulnerability scan, dark web scan, anti-ransomeware/malware software, and image-level backups. We want people to understand that partnering with Brightmoor Partners gives them “Elevated Peace of Mind” (tagline). Current badge and logos uploaded.

Target Market(s)

Small businesses

Contact Information for Business Card

Lena Marwick, Vice President, lena@brightmoorpartners.example, 555-806-1937, www.brightmoorpartners.example

Requirements
Nice to have
• I do prefer the darker background for front and back

```html
<!DOCTYPE html>
<html lang="en">
<head>
<meta charset="utf-8">
<title>Brightmoor Partners – Business Card</title>
<link rel="stylesheet" href="https://fonts.googleapis.com/css2?family=Open+Sans:ital,wght@0,400;0,600;0,700;1,400;1,700&display=swap">
<style>
  :root {
    --scene: #1c1c1c;
    --card-dark: #141414;
    --brand-red: #e3202a;
    --text-light: #d6d6d6;
    --text-white: #ffffff;
  }
  * { margin: 0; padding: 0; box-sizing: border-box; }
  html, body { width: 1200px; height: 900px; overflow: hidden; }
  body {
    background: var(--scene);
    font-family: "Open Sans", Arial, sans-serif;
    display: flex;
    align-items: center;
    justify-content: center;
    gap: 40px;
  }
  .card {
    width: 540px;
    height: 309px;
    border-radius: 4px;
    position: relative;
    overflow: hidden;
    background: var(--card-dark);
    box-shadow: 0 18px 40px rgba(0,0,0,.6), 0 0 0 1px rgba(255,255,255,.04);
  }

  /* Front: contact side */
  .contact {
    position: absolute;
    left: 36px;
    top: 40px;
    width: 300px;
  }
  .contact-name {
    color: var(--brand-red);
    font-weight: 700;
    font-style: italic;
    text-transform: uppercase;
    font-size: 22px;
    letter-spacing: .3px;
    line-height: 1.1;
  }
  .contact-title {
    color: var(--text-light);
    font-style: italic;
    font-size: 15px;
    margin-top: 2px;
  }
  .divider {
    width: 40px;
    height: 2px;
    background: var(--brand-red);
    margin: 22px 0 20px;
  }
  .address {
    color: var(--text-light);
    font-size: 14px;
    line-height: 1.35;
    margin-bottom: 14px;
  }
  .contact-list { list-style: none; }
  .contact-list li {
    display: flex;
    align-items: center;
    gap: 8px;
    color: var(--text-light);
    font-size: 13.5px;
    line-height: 1.45;
    white-space: nowrap;
  }
  .contact-list svg { width: 11px; height: 11px; fill: var(--brand-red); flex: none; }

  .front-mark {
    position: absolute;
    right: 34px;
    top: 50%;
    transform: translateY(-50%);
    display: flex;
    flex-direction: column;
    align-items: center;
    gap: 14px;
  }
  .mark-square {
    width: 140px;
    height: 140px;
    background: var(--brand-red);
  }
  .mark-name {
    color: var(--text-white);
    font-weight: 600;
    font-size: 15px;
    letter-spacing: 4px;
    text-transform: uppercase;
  }

  /* Back: brand side */
  .card-back {
    display: flex;
    align-items: center;
    justify-content: center;
    gap: 18px;
  }
  .back-square {
    width: 44px;
    height: 44px;
    background: var(--brand-red);
    flex: none;
  }
  .back-name {
    color: var(--text-white);
    font-weight: 600;
    font-size: 24px;
    letter-spacing: 6px;
    text-transform: uppercase;
    white-space: nowrap;
  }
</style>
</head>
<body>

  <section class="card card-front" aria-label="Business card front">
    <div class="contact">
      <h1 class="contact-name">Lena Marwick</h1>
      <p class="contact-title">Vice President</p>
      <div class="divider"></div>
      <p class="address">2480 Harborview Lane<br>Seacliff CA 90000</p>
      <ul class="contact-list">
        <li>
          <svg viewBox="0 0 12 12" aria-hidden="true"><path d="M2.4 0.6l2 2.2-1.1 1.3c.8 1.7 2 2.9 3.7 3.7l1.3-1.1 2.2 2-1.2 2.1C5.2 10.6 1.4 6.8 0.3 1.8z"/></svg>
          555-806-1937
        </li>
        <li>
          <svg viewBox="0 0 12 12" aria-hidden="true"><path d="M0 2h12v1L6 7 0 3z"/><path d="M0 4.3l6 4 6-4V10H0z"/></svg>
          lena@brightmoorpartners.example
        </li>
        <li>
          <svg viewBox="0 0 12 12" aria-hidden="true"><circle cx="6" cy="6" r="6"/><path d="M0 6h12M6 0c-2.5 3-2.5 9 0 12M6 0c2.5 3 2.5 9 0 12" stroke="#141414" stroke-width=".9" fill="none"/></svg>
          www.brightmoorpartners.example
        </li>
      </ul>
    </div>
    <div class="front-mark">
      <div class="mark-square"></div>
      <span class="mark-name">Brightmoor</span>
    </div>
  </section>

  <section class="card card-back" aria-label="Business card back">
    <div class="back-square"></div>
    <span class="back-name">Brightmoor Partners</span>
  </section>

</body>
</html>
```